New Church Home Page and Content Page Design

Our church, Cedar Hollow Baptist Church www.chbcfenway.example, needs an update for our online presence. The homepage design should provide the following 4 pieces of information above the fold:
1. Church location - 47 Linden Brook Lane in Chappaqua, NY, USA.
2. Service times and types Sunday school, children's church, etc..
3. A space for some text describing us and our beliefs - a Bible believing independent Baptist church.
4. photos of our members to give visitors an impression of what kind of people attend our church - a friendly group of culturally diverse people who love Jesus.

In addition to the homepage we need a design for internal pages of general content. The content page design should provide a lot of room for content and prominent navigation area. We will use this design to host pages with content such as:
A full description of our beliefs
A photo gallery
An event calendar
Embedded audio and video of past sermons
A member directory
etc.
Updates

Thanks everyone for your submissions. I'll be meeting with our Pastor tomorrow. I am working as fast as I can to review all the designs and come up with a short list for him. A decision should be close behind.

Target Market(s)

Local people looking for a church.

Industry/Entity Type

Church

Requirements
Must have
• 1. Place to show church location - Westchester county, New York State, USA.
2. Place to list service times and types.
3. A space for some text describing us and our beliefs.
4. A place to display photos of our members (see also the nice to have section)
Nice to have
• Would be great if the member photos (#4 in must have section) displayed the images in some innovative way. I rather not have an ordinary carousel of images.

```html
<!DOCTYPE html>
<html lang="en">
<head>
<meta charset="utf-8">
<title>Cedar Hollow Baptist Church</title>
<link rel="stylesheet" href="https://fonts.googleapis.com/css2?family=Carlito:ital,wght@0,400;0,700;1,400;1,700&family=Open+Sans:wght@400;600&display=swap">
<style>
:root{
  --navy:#1b3557;
  --navy-deep:#16304f;
  --band:#e3e3e3;
  --line:#d9d9d9;
  --text:#5a5a5a;
  --muted:#8a9bb3;
  --white:#ffffff;
  --black:#111111;
  --name-bar:#d7d7d7;
}
*{box-sizing:border-box;margin:0;padding:0}
html,body{width:1200px;height:1129px;overflow:hidden;background:var(--white)}
body{position:relative;font-family:"Open Sans",Arial,sans-serif;color:var(--text);font-size:7px}
.abs{position:absolute}

/* header */
.brand{left:0;width:1200px;top:16px;display:flex;justify-content:center;align-items:center;gap:8px}
.brand-mark{width:14px;height:14px;background:var(--navy)}
.brand-name{font-family:"Carlito",sans-serif;font-weight:700;font-size:11px;line-height:11px;color:var(--navy)}
.header-rule{left:0;top:69px;width:1200px;height:1px;background:#ececec}
.main-nav{left:0;width:1200px;top:79px;display:flex;justify-content:center;font-size:7px;text-transform:uppercase;color:#444}
.main-nav a{color:inherit;text-decoration:none;padding:0 9px;border-left:1px solid #ccc;line-height:9px}
.main-nav a:first-child{border-left:none;color:var(--navy)}

/* hero */
.gray-band{left:0;top:297px;width:1200px;height:121px;background:var(--band)}
.hero-photo{left:286px;top:99px;width:428px;height:236px;background:radial-gradient(ellipse at 72% 28%,#dfe9f4 0%,#7b8aa0 18%,#3b3236 45%,#120f12 80%)}
.hero-caption{left:286px;top:297px;width:428px;height:38px;background:rgba(20,28,42,.55)}
.hero-caption-text{left:307px;top:310px;width:350px;white-space:nowrap;overflow:hidden;color:var(--white);font-family:"Carlito",sans-serif;font-size:9.2px;letter-spacing:0;line-height:12px}
.circle-btn{width:17px;height:17px}
.events{left:714px;top:99px;width:185px;height:236px;background:var(--navy);color:var(--white)}
.events-title{position:absolute;top:20px;width:100%;text-align:center;font-family:"Carlito",sans-serif;font-size:10px;letter-spacing:.4px}
.event{position:absolute;left:18px;display:flex;gap:11px}
.event-date{width:21px;text-align:center}
.event-day{display:block;background:var(--white);color:var(--muted);font-family:"Carlito",sans-serif;font-size:13px;line-height:19px}
.event-month{display:block;font-size:7px;color:#c9d3e0;margin-top:2px}
.event-title{font-family:"Carlito",sans-serif;font-size:9px;color:#eef2f7;margin-bottom:3px}
.event-meta{font-size:6px;color:#9fb0c6;line-height:11px}
.events-rule{position:absolute;left:15px;right:30px;top:216px;height:1px;background:#3f5777}

.sermon-label{left:286px;top:348px;font-family:"Carlito",sans-serif;font-style:italic;font-weight:700;font-size:7px;color:#222}
.sermon-quote{left:286px;top:362px;width:420px;font-family:"Carlito",sans-serif;font-size:12.5px;line-height:15px;color:var(--navy)}
.download-btn{left:752px;top:358px;width:115px;height:27px;background:var(--black);color:var(--white);font-size:6px;text-transform:uppercase;display:flex;align-items:center;justify-content:center}

/* intro panel */
.intro-panel{left:286px;top:401px;width:613px;height:153px;background:var(--white);box-shadow:0 -1px 6px rgba(0,0,0,.06)}
.feature{position:absolute;top:20px;width:131px}
.feature-photo{height:68px;position:relative}
.read-more{position:absolute;left:-1px;top:46px;background:var(--navy);color:var(--white);font-size:6px;padding:3px 9px}
.feature-title{margin-top:17px;font-family:"Carlito",sans-serif;font-weight:400;font-size:9px;color:var(--navy);text-transform:uppercase}
.feature-text{margin-top:5px;font-size:6px;line-height:8.5px;width:150px}
.community{position:absolute;left:466px;top:18px;width:135px}
.community-title{font-family:"Carlito",sans-serif;font-weight:400;font-size:9px;color:var(--navy);text-transform:uppercase}
.community-text{margin-top:7px;font-size:6px;line-height:8.5px}
.community-quote{margin-top:10px;font-family:"Carlito",sans-serif;font-size:9.5px;line-height:11px;color:var(--navy)}
.community-cite{margin-top:9px;font-family:"Carlito",sans-serif;font-style:italic;font-size:8.5px;color:var(--navy)}
.section-rule{left:286px;top:554px;width:613px;height:1px;background:var(--line)}

/* news & gallery */
.section-title{font-family:"Carlito",sans-serif;font-weight:400;font-size:9px;color:var(--navy);text-transform:uppercase;display:flex;align-items:center;gap:6px}
.news-item{position:absolute;width:220px;height:58px}
.news-thumb{position:absolute;left:0;top:0;width:76px;height:58px;border:1px solid #e6e6e6;padding:4px;background:var(--white)}
.news-thumb span{display:block;width:100%;height:100%;background:linear-gradient(135deg,#cfd3d6,#e8dcd4 50%,#c24a52 90%)}
.news-body{position:absolute;left:85px;top:0;width:135px}
.news-title{font-family:"Carlito",sans-serif;font-weight:400;font-size:9px;color:#555}
.news-text{margin-top:5px;font-size:6px;line-height:8px;color:#888}
.news-more{margin-top:6px;font-size:5.5px;color:#888}
.news-rule{left:286px;top:666px;width:447px;height:1px;background:var(--line)}
.gallery-tile{position:absolute;width:71px;height:63px}

/* members */
.members-band{left:0;top:773px;width:1200px;height:177px;background:var(--navy)}
.members-title{left:357px;top:796px;width:463px;display:flex;align-items:center;gap:8px;color:var(--white);font-family:"Carlito",sans-serif;font-weight:400;font-size:9px}
.members-title .rule{flex:1;height:1px;background:#4f6b8d}
.member{position:absolute;top:828px;width:111px}
.member-photo{height:73px;border:4px solid var(--white);background:var(--white)}
.member-photo span{display:block;height:100%}
.member-name{height:16px;background:var(--name-bar);font-family:"Carlito",sans-serif;font-size:9px;color:#333;padding:3px 0 0 18px;position:relative}
.member-name::before{content:"";position:absolute;left:12px;top:0;border:4px solid transparent;border-top-color:var(--navy)}
.band-arrow{top:863px}

/* footer */
.footer-title{font-family:"Carlito",sans-serif;font-weight:400;font-size:9px;color:var(--navy);text-transform:uppercase;display:flex;align-items:center;gap:6px}
.newsletter-note{left:286px;top:986px;font-size:6px;color:#888}
.email-field{left:286px;top:1001px;width:113px;height:22px;border:1px solid #cfcfcf;font-size:6px;color:#aaa;padding:7px 8px}
.social{left:286px;top:1066px;display:flex;gap:8px}
.social span{width:9px;height:9px;border-radius:50%;background:var(--navy)}
.services{left:472px;top:990px;font-size:6.5px;line-height:8.5px;color:#666}
.services p+p{margin-top:8px}
.map{left:571px;top:966px;width:328px;height:113px;background:linear-gradient(160deg,#ece9e2,#e2ded5)}
.map-label{left:571px;top:978px;width:328px;text-align:center;font-family:"Carlito",sans-serif;font-size:9px;color:var(--navy)}
.footer-rule{left:286px;top:1095px;width:613px;height:1px;background:#e3e3e3}
.legal{top:1108px;font-size:5.5px;color:#555}
</style>
</head>
<body>

<header>
  <div class="abs brand">
    <span class="brand-mark"></span>
    <div class="brand-name">Cedar Hollow<br>Baptist<br>Church</div>
  </div>
  <div class="abs header-rule"></div>
  <nav class="abs main-nav">
    <a href="#">Home</a><a href="#">Calender</a><a href="#">Ministries</a><a href="#">Service Timing</a><a href="#">Sermons</a><a href="#">Contact Us</a>
  </nav>
</header>

<section>
  <div class="abs gray-band"></div>
  <div class="abs hero-photo" role="img" aria-label="White dove flying against dark clouds with sunlight breaking through"></div>
  <div class="abs hero-caption"></div>
  <p class="abs hero-caption-text">DOUBTS ARE THE ANTS IN THE PANTS OF FAITH. THEY KEEP IT AWAKE AND MOVING.</p>
  <svg class="abs circle-btn" style="left:666px;top:307px" viewBox="0 0 17 17"><circle cx="8.5" cy="8.5" r="7.5" fill="none" stroke="#8fa3bd" stroke-width="1"/><path d="M10 5 6.5 8.5 10 12" fill="none" stroke="#8fa3bd" stroke-width="1.4"/></svg>
  <svg class="abs circle-btn" style="left:689px;top:307px" viewBox="0 0 17 17"><circle cx="8.5" cy="8.5" r="7.5" fill="#5a5a5a" stroke="#ddd" stroke-width="1"/><path d="M7 5 10.5 8.5 7 12" fill="none" stroke="#fff" stroke-width="1.4"/></svg>

  <aside class="abs events">
    <div class="events-title">UPCOMING EVENTS</div>
    <div class="event" style="top:55px">
      <div class="event-date"><span class="event-day">04</span><span class="event-month">MAY</span></div>
      <div><div class="event-title">Upcoming Heading Here</div><div class="event-meta">Los Angel, Bird Way<br>10.20</div></div>
    </div>
    <div class="event" style="top:108px">
      <div class="event-date"><span class="event-day">12</span><span class="event-month">MAY</span></div>
      <div><div class="event-title">Upcoming Heading Here</div><div class="event-meta">Los Angel, Bird Way<br>10.20</div></div>
    </div>
    <div class="event" style="top:160px">
      <div class="event-date"><span class="event-day">18</span><span class="event-month">MAY</span></div>
      <div><div class="event-title">Upcoming Heading Here</div><div class="event-meta">Los Angel, Bird Way<br>10.20</div></div>
    </div>
    <div class="events-rule"></div>
    <svg class="circle-btn" style="position:absolute;left:156px;top:207px" viewBox="0 0 17 17"><circle cx="8.5" cy="8.5" r="7.5" fill="none" stroke="#6d84a3" stroke-width="1"/><path d="M7 5 10.5 8.5 7 12" fill="none" stroke="#c9d3e0" stroke-width="1.4"/></svg>
  </aside>

  <div class="abs sermon-label">Latest Sermon: The Open Invitation - 04 May 2014</div>
  <p class="abs sermon-quote">Blessed is the man that endureth temptation for when he is tried he shall receive the crown of life.</p>
  <div class="abs download-btn">Download the latest sermon</div>
</section>

<section class="abs intro-panel">
  <article class="feature" style="left:14px">
    <div class="feature-photo" role="img" aria-label="Wooden pier stretching into a lake at sunset" style="background:linear-gradient(180deg,#e6b46a,#d99a55 40%,#5d8a8e 75%,#3d6a70)"><span class="read-more">read more</span></div>
    <h3 class="feature-title">About Us</h3>
    <p class="feature-text">Lorem Ipsum is simply dummy text of the printing and typesetting industry.</p>
  </article>
  <article class="feature" style="left:163px">
    <div class="feature-photo" role="img" aria-label="Black and white photo of a cathedral facade" style="background:linear-gradient(180deg,#9a9a9a,#4a4a4a 60%,#2a2a2a)"><span class="read-more">read more</span></div>
    <h3 class="feature-title">Sermons</h3>
    <p class="feature-text">Lorem Ipsum is simply dummy text of the printing and typesetting industry.</p>
  </article>
  <article class="feature" style="left:312px">
    <div class="feature-photo" role="img" aria-label="Wooden cross pendant held in a hand" style="background:linear-gradient(135deg,#c9a08a,#a5705a 50%,#6e4a3c)"><span class="read-more">read more</span></div>
    <h3 class="feature-title">Ministries</h3>
    <p class="feature-text">Lorem Ipsum is simply dummy text of the printing and typesetting industry.</p>
  </article>
  <div class="community">
    <h3 class="community-title">Join Our Community</h3>
    <p class="community-text">Lorem Ipsum is simply dummy text of the printing and typesetting industry. Lorem Ipsum has been the industry's standard dummy text ever since the 1500s</p>
    <p class="community-quote">“ Blessed is the man that endureth temptation for when he is tried he shall receive the crown of life. ”</p>
    <p class="community-cite">- Harold Winslow</p>
  </div>
</section>
<div class="abs section-rule"></div>

<section>
  <h2 class="abs section-title" style="left:286px;top:572px">Church News &amp; Announcements
    <svg width="13" height="13" viewBox="0 0 13 13"><circle cx="6.5" cy="6.5" r="5.8" fill="none" stroke="#777"/><path d="M5.3 4 7.8 6.5 5.3 9" fill="none" stroke="#777" stroke-width="1.1"/></svg></h2>

  <article class="news-item" style="left:286px;top:596px">
    <div class="news-thumb" role="img" aria-label="Young child in a striped shirt"><span></span></div>
    <div class="news-body"><h4 class="news-title">News Heading Here</h4><p class="news-text">Lorem ipsum dolor sit amet, consectetur adipiscing elit. Nulla iaculis aliquet augue, eu varius purus sollicitudin eget.</p><p class="news-more">read more</p></div>
  </article>
  <article class="news-item" style="left:521px;top:596px">
    <div class="news-thumb" role="img" aria-label="Young child in a striped shirt"><span></span></div>
    <div class="news-body"><h4 class="news-title">News Heading Here</h4><p class="news-text">Lorem ipsum dolor sit amet, consectetur adipiscing elit. Nulla iaculis aliquet augue, eu varius purus sollicitudin eget.</p><p class="news-more">read more</p></div>
  </article>
  <div class="abs news-rule"></div>
  <article class="news-item" style="left:286px;top:678px">
    <div class="news-thumb" role="img" aria-label="Young child in a striped shirt"><span></span></div>
    <div class="news-body"><h4 class="news-title">News Heading Here</h4><p class="news-text">Lorem ipsum dolor sit amet, consectetur adipiscing elit. Nulla iaculis aliquet augue, eu varius purus sollicitudin eget.</p><p class="news-more">read more</p></div>
  </article>
  <article class="news-item" style="left:521px;top:678px">
    <div class="news-thumb" role="img" aria-label="Young child in a striped shirt"><span></span></div>
    <div class="news-body"><h4 class="news-title">News Heading Here</h4><p class="news-text">Lorem ipsum dolor sit amet, consectetur adipiscing elit. Nulla iaculis aliquet augue, eu varius purus sollicitudin eget.</p><p class="news-more">read more</p></div>
  </article>

  <h2 class="abs section-title" style="left:752px;top:572px">Gallery
    <svg width="13" height="13" viewBox="0 0 13 13"><circle cx="6.5" cy="6.5" r="5.8" fill="none" stroke="#777"/><path d="M5.3 4 7.8 6.5 5.3 9" fill="none" stroke="#777" stroke-width="1.1"/></svg></h2>
  <div class="gallery-tile" role="img" aria-label="Wooden cross in a hand" style="left:752px;top:596px;background:linear-gradient(135deg,#c29a85,#8a5e4a)"></div>
  <div class="gallery-tile" role="img" aria-label="Pier on a lake at sunset" style="left:828px;top:596px;background:linear-gradient(180deg,#e0a862,#6d9292)"></div>
  <div class="gallery-tile" role="img" aria-label="Smiling child portrait" style="left:752px;top:664px;background:linear-gradient(135deg,#6a4a36,#3e2a20)"></div>
  <div class="gallery-tile" role="img" aria-label="Close-up of red leaves" style="left:828px;top:664px;background:linear-gradient(135deg,#d2406a,#8c1c3e)"></div>
</section>

<section>
  <div class="abs members-band"></div>
  <h2 class="abs members-title">
    <span class="rule"></span>OUR MEMBERS<span class="rule"></span>
  </h2>
  <svg class="abs band-arrow" style="left:333px" width="10" height="16" viewBox="0 0 10 16"><path d="M8 1 2 8 8 15" fill="none" stroke="#4f6b8d" stroke-width="1.3"/></svg>
  <svg class="abs band-arrow" style="left:833px" width="10" height="16" viewBox="0 0 10 16"><path d="M2 1 8 8 2 15" fill="none" stroke="#4f6b8d" stroke-width="1.3"/></svg>
  <figure class="member" style="left:357px">
    <div class="member-photo"><span role="img" aria-label="Portrait of member Lisa Alizabeth" style="background:linear-gradient(135deg,#3a6ea5,#d9b58a 60%,#e8d2a0)"></span></div>
    <figcaption class="member-name">Lisa Alizabeth</figcaption>
  </figure>
  <figure class="member" style="left:474px">
    <div class="member-photo"><span role="img" aria-label="Portrait of member Dania Harbert" style="background:linear-gradient(135deg,#f2f2f2,#c88a66 60%,#6b3e2a)"></span></div>
    <figcaption class="member-name">Dania Harbert</figcaption>
  </figure>
  <figure class="member" style="left:592px">
    <div class="member-photo"><span role="img" aria-label="Portrait of member Robert D" style="background:linear-gradient(135deg,#5fc3d2,#d9a98a 55%,#7ac7d1)"></span></div>
    <figcaption class="member-name">Robert D</figcaption>
  </figure>
  <figure class="member" style="left:709px">
    <div class="member-photo"><span role="img" aria-label="Portrait of member Joan Tonren" style="background:linear-gradient(135deg,#d9dde2,#e6c58a 50%,#c6ccd4)"></span></div>
    <figcaption class="member-name">Joan Tonren</figcaption>
  </figure>
</section>

<footer>
  <h3 class="abs footer-title" style="left:286px;top:966px">
    <svg width="14" height="10" viewBox="0 0 14 10"><rect x=".5" y=".5" width="13" height="9" fill="none" stroke="#777"/><path d="M.5 .5 7 6 13.5 .5" fill="none" stroke="#777"/></svg>Newsletter</h3>
  <p class="abs newsletter-note">Sign Up to receive our email updates</p>
  <div class="abs email-field">Your Email</div>
  <h3 class="abs footer-title" style="left:286px;top:1045px">Follow Us</h3>
  <div class="abs social" aria-label="Social media links">
    <span></span><span></span><span></span><span></span><span></span><span></span>
  </div>

  <h3 class="abs footer-title" style="left:449px;top:965px">
    <svg width="13" height="13" viewBox="0 0 13 13"><circle cx="6.5" cy="6.5" r="5.8" fill="none" stroke="#777"/><path d="M6.5 3v3.5l2 1.5" fill="none" stroke="#777"/></svg>Church Services</h3>
  <div class="abs services">
    <p>Sunday &nbsp;Prayer<br>10.00 am.<br>3.00 pm.<br>6.00 pm.</p>
    <p>All Day Prayer<br>10.00 am.<br>3.00 pm.<br>6.00 pm.</p>
  </div>

  <div class="abs map" role="img" aria-label="Street map showing the church location"></div>
  <div class="abs map-label">LOCATION : <b>47 Linden Brook Lane</b> Chappaqua, NY, USA.</div>
  <svg class="abs" style="left:698px;top:1003px" width="10" height="15" viewBox="0 0 10 15"><path d="M5 14C5 14 1 8.5 1 5a4 4 0 0 1 8 0c0 3.5-4 9-4 9z" fill="#d9262b"/><circle cx="5" cy="5" r="1.5" fill="#fff"/></svg>

  <div class="abs footer-rule"></div>
  <p class="abs legal" style="left:286px">Copyright © 2014. Company Name. All rights reserved</p>
  <p class="abs legal" style="left:857px">Privacy Policy</p>
</footer>

</body>
</html>
```